Product Catalog for Ski Guiding Company

ZEPHYRPRESS LINK:
https://zephyrpress.example.jp/templates/

We need a 24-page A5 size catalog design for our ski tours in Japan.

Here is the folder with the wordings and pictures.

https://files.example.net/open?id=7Xq2Lm-PwTz4NvR8KdHs3YcE

Please also check the link below for the format.

For your reference, I have attached some pages from last years catalog. We would like a new design though.

LINK FOR Comparison Chart
http://frostpeakguides.example.com/multi-day-tours/multi-day-trip-comparison/
http://frostpeakguides.example.com/backcountry-day-tours/day-tour-comparison/

Target Market(s)

English speaking skiers and snowboarders

Font styles to use
Serif

Colors
0655a3

Requirements
Must have
• Pictures are very key so please make sure that the skier or snowboarder is shown
• Please also include page numbers on the bottom corner
• Please also send at least 6 pages for sample
Should not have
• Letters in the color red

```html
<!DOCTYPE html>
<html lang="en">
<head>
<meta charset="utf-8">
<title>Kitakaze Snowcats – Catalog Spread</title>
<link href="https://fonts.googleapis.com/css2?family=Cinzel:wght@400;500&family=Open+Sans:wght@400;600&family=Montserrat:wght@600;700&display=swap" rel="stylesheet">
<style>
  :root {
    --backdrop: #8a8b8c;
    --brand-blue: #0655a3;
    --tab-red: #b01e2a;
    --tab-dark: #2a2c30;
    --white: #ffffff;
    --sky-top: #2f6eb0;
    --sky-mid: #6e9ccc;
    --snow: #d6dee8;
    --ridge: #6b7384;
    --land: #3a3d44;
    --water: #1d2c44;
  }
  * { box-sizing: border-box; margin: 0; padding: 0; }
  html, body { width: 1200px; height: 800px; overflow: hidden; }
  body { background: var(--backdrop); position: relative; font-family: "Open Sans", sans-serif; }

  .spread {
    position: absolute; left: 50px; top: 10px; width: 1100px; height: 780px;
    overflow: hidden; box-shadow: 0 6px 18px rgba(0,0,0,.35);
  }
  .spread__photo {
    position: absolute; inset: 0;
    background:
      radial-gradient(ellipse 420px 90px at 760px 330px, rgba(236,241,247,.85), rgba(236,241,247,0) 100%),
      radial-gradient(ellipse 360px 80px at 380px 360px, rgba(226,233,242,.75), rgba(226,233,242,0) 100%),
      radial-gradient(ellipse 260px 60px at 960px 610px, rgba(120,160,205,.45), rgba(120,160,205,0) 100%),
      linear-gradient(180deg,
        var(--sky-top) 0%, #4f86c0 25%, var(--sky-mid) 36%, var(--snow) 44%,
        var(--ridge) 51%, var(--land) 58%, #2a3a52 64%, var(--water) 74%,
        #2c4e78 88%, #3d6796 100%);
  }
  .spread__fold {
    position: absolute; left: 550px; top: 0; bottom: 0; width: 1px;
    background: rgba(255,255,255,.18);
  }

  .intro { position: absolute; left: 42px; top: 52px; width: 470px; color: var(--white); }
  .intro__title {
    font-family: "Cinzel", serif; font-weight: 400; font-size: 30px; letter-spacing: 1px;
    display: flex; align-items: center; gap: 14px; white-space: nowrap;
  }
  .intro__rule { flex: 1; height: 1px; background: var(--white); margin-top: 6px; }
  .intro__text { margin-top: 18px; font-size: 10.5px; line-height: 1.32; }
  .intro__text + .intro__text { margin-top: 12px; }

  .stats {
    position: absolute; left: 58px; top: 500px; display: flex; gap: 2px;
    align-items: flex-start; list-style: none;
  }
  .stat { width: 92px; display: flex; flex-direction: column; align-items: center; text-align: center; color: var(--white); }
  .stat__value {
    width: 78px; height: 78px; border-radius: 50%; background: var(--brand-blue);
    display: flex; align-items: center; justify-content: center; text-align: center;
    font-family: "Montserrat", sans-serif; font-weight: 700; font-size: 20px; line-height: 1.05;
  }
  .stat__value--small { font-size: 14px; }
  .stat__label { margin-top: 8px; font-size: 11px; line-height: 1.3; }

  .club { position: absolute; right: 52px; top: 46px; display: flex; align-items: center; gap: 10px; color: var(--white); }
  .club__dot { width: 34px; height: 34px; border-radius: 50%; background: var(--tab-dark); }
  .club__name { font-size: 12px; font-weight: 600; letter-spacing: 1px; line-height: 1.3; }

  .page-tab { position: absolute; bottom: 0; width: 240px; height: 40px; }
  .page-tab--left { left: 0; }
  .page-tab--right { right: 0; }
  .page-tab__number {
    position: absolute; bottom: 10px; font-family: "Montserrat", sans-serif;
    font-weight: 700; font-size: 15px; color: var(--white);
  }
  .page-tab--left .page-tab__number { left: 182px; }
  .page-tab--right .page-tab__number { right: 182px; }
</style>
</head>
<body>
  <main class="spread">
    <div class="spread__photo" role="img" aria-label="Snow-covered mountain range spanning both pages beneath a blue sky, seen across a rocky tidal shoreline with calm reflective water"></div>
    <div class="spread__fold"></div>

    <section class="intro">
      <h1 class="intro__title">Kitakaze Snowcats <span class="intro__rule"></span></h1>
      <p class="intro__text">After 10 years of searching and knowing that given Hokkaido's incredible snow, ideal terrain, and perfect tree skiing, a place to rival Canadian cat ski operations had to exist. Together with the town of Shimamaki, we are celebrating the 4th year of the rebirth of cat skiing on the Kariba mountain range and bringing new life to this small fishing town.</p>
      <p class="intro__text">Kitakaze Snowcats delivers a combination of world class powder skiing and snowboarding with a rural Japanese cultural experience like no other. Dine on fine powder in the day, fresh seafood at night and wash it all down with an authentic Japanese sake or beer. Finish with a soak in the natural hotspring and repeat.</p>
    </section>

    <ul class="stats">
      <li class="stat"><div class="stat__value">6-13</div><p class="stat__label">Runs per day</p></li>
      <li class="stat"><div class="stat__value stat__value--small">450m/<br>1477ft</div><p class="stat__label">Average<br>vertical / run</p></li>
      <li class="stat"><div class="stat__value">15-35</div><p class="stat__label">Slope angle</p></li>
      <li class="stat"><div class="stat__value stat__value--small">6,500m<br>/21,325ft</div><p class="stat__label">Max vertical<br>recorded in a day</p></li>
      <li class="stat"><div class="stat__value">2<br>hours</div><p class="stat__label">Drive time<br>from Niseko</p></li>
    </ul>

    <div class="club">
      <span class="club__dot"></span>
      <span class="club__name">NORTHRIDGE<br>BACKCOUNTRY CLUB</span>
    </div>

    <div class="page-tab page-tab--left">
      <svg width="240" height="40" viewBox="0 0 240 40" aria-hidden="true">
        <polygon points="0,8 150,8 146,12 0,12" fill="var(--tab-dark)"/>
        <polygon points="0,12 222,4 240,40 0,40" fill="var(--tab-red)"/>
      </svg>
      <span class="page-tab__number">8</span>
    </div>
    <div class="page-tab page-tab--right">
      <svg width="240" height="40" viewBox="0 0 240 40" aria-hidden="true">
        <polygon points="90,8 240,8 240,12 94,12" fill="var(--tab-dark)"/>
        <polygon points="18,4 240,12 240,40 0,40" fill="var(--tab-red)"/>
      </svg>
      <span class="page-tab__number">9</span>
    </div>
  </main>
</body>
</html>
```